Property developer, money partner needs business card design using logo concept provided

Our company develops residential properties, does money lends for joint ventures in property deals and finds property deals for other money partners. We have provided a basic logo for you to work from. Any graphic or logo design on the card is to communicate development and finance collaboration. Color choice is not so important for us, but color choice does need to reflect professionalism.

```html
<!DOCTYPE html>
<html lang="en">
<head>
<meta charset="utf-8">
<title>Oakline Property Partners – Business Card</title>
<link rel="stylesheet" href="https://fonts.googleapis.com/css2?family=Lato:wght@400;700;900&family=Montserrat:wght@500;800&family=Yellowtail&display=swap">
<style>
  :root {
    --page-bg: #ecebe8;
    --blue-top: #0a72b8;
    --blue-deep: #0b3f86;
    --navy: #1b3a84;
    --mist: #e6ecf4;
    --red: #9b0a0e;
    --grey-band: #8d8d8d;
    --rule-grey: #9a9a9a;
    --ink: #2a2a2a;
    --white: #ffffff;
  }
  html, body {
    margin: 0;
    width: 1047px;
    height: 1200px;
    overflow: hidden;
    background: var(--page-bg);
    font-family: "Lato", sans-serif;
  }
  .card {
    position: absolute;
    left: 138px;
    width: 770px;
    height: 440px;
    border-radius: 20px;
    overflow: hidden;
    background: var(--white);
    box-shadow: 0 6px 16px rgba(0,0,0,0.18);
  }
  .card--front { top: 120px; }
  .card--back { top: 640px; }
  .card svg.bg { position: absolute; left: 0; top: 0; }

  /* front */
  .holder-name {
    position: absolute; left: 38px; top: 214px;
    margin: 0; color: var(--white);
    font-weight: 900; font-size: 39px; line-height: 1; letter-spacing: 0.3px;
  }
  .holder-role {
    position: absolute; left: 38px; top: 260px;
    margin: 0; color: var(--white); font-size: 21px; line-height: 1.2;
  }
  .contact {
    position: absolute; left: 38px; top: 326px;
    margin: 0; padding: 0; list-style: none; color: var(--white);
  }
  .contact li { display: flex; align-items: center; gap: 10px; height: 27px; }
  .contact .phone { font-size: 20px; }
  .contact .email { font-size: 17px; }
  .contact svg { width: 15px; height: 15px; flex: none; }
  .address {
    position: absolute; right: 38px; top: 330px;
    margin: 0; text-align: right; color: var(--ink);
    font-size: 17px; line-height: 26px; font-style: normal;
  }
  .website {
    position: absolute; right: 28px; top: 408px;
    color: var(--white); font-size: 17px; line-height: 1.2;
  }
  .front-mark {
    position: absolute; left: 440px; top: 130px; width: 280px;
    display: flex; align-items: center; justify-content: center; gap: 10px;
    color: var(--navy); font-family: "Lato", sans-serif;
    font-weight: 900; font-size: 32px; letter-spacing: 2px;
  }
  .front-mark .square { width: 22px; height: 22px; background: var(--navy); }

  /* back */
  .brand-dot {
    position: absolute; left: 492px; top: 80px;
    width: 124px; height: 124px; border-radius: 50%;
    background: linear-gradient(180deg, #1a78c4, var(--navy));
  }
  .brand-name {
    position: absolute; left: 370px; top: 248px; width: 370px;
    margin: 0; text-align: center; font-family: "Montserrat", sans-serif; font-weight: 800;
    font-size: 38px; line-height: 1; letter-spacing: 9px; color: var(--navy);
  }
  .brand-sub {
    position: absolute; left: 370px; top: 294px; width: 370px;
    margin: 0; text-align: center; font-family: "Montserrat", sans-serif; font-weight: 500;
    font-size: 15px; line-height: 1; letter-spacing: 8px; color: var(--ink);
  }
  .brand-acn {
    position: absolute; left: 370px; top: 316px; width: 370px;
    display: flex; align-items: center; justify-content: center; gap: 8px;
    font-size: 12px; line-height: 16px; letter-spacing: 4px; color: var(--ink);
  }
  .brand-acn::before, .brand-acn::after {
    content: ""; width: 56px; height: 1.5px; background: var(--ink);
  }
  .tagline {
    position: absolute; left: 340px; top: 372px; width: 410px;
    margin: 0; text-align: center; font-family: "Yellowtail", cursive;
    font-size: 29px; line-height: 1.2; white-space: nowrap;
  }
  .tagline .lead { color: var(--navy); }
  .tagline .rest { color: var(--red); }
</style>
</head>
<body>

<section class="card card--front" aria-label="Business card front">
  <svg class="bg" width="770" height="440" viewBox="0 0 770 440" aria-hidden="true">
    <defs>
      <linearGradient id="frontBlue" x1="0" y1="0" x2="0" y2="1">
        <stop offset="0" stop-color="#0a72b8"/>
        <stop offset="1" stop-color="#0b3f86"/>
      </linearGradient>
    </defs>
    <rect width="770" height="440" fill="url(#frontBlue)"/>
    <polygon points="0,405 365,405 355,420 0,420" fill="var(--red)"/>
    <polygon points="0,420 355,420 348,440 0,440" fill="var(--grey-band)"/>
  </svg>
  <svg class="bg" width="770" height="440" viewBox="0 0 770 440" role="img" aria-label="Area for a soft pale illustration of a thinking head beside the brand">
    <defs>
      <linearGradient id="mistFade" x1="0" y1="0" x2="1" y2="0">
        <stop offset="0" stop-color="#dfe8f3"/>
        <stop offset="1" stop-color="#ffffff"/>
      </linearGradient>
    </defs>
    <rect x="400" y="0" width="370" height="400" fill="url(#mistFade)"/>
  </svg>
  <svg class="bg" width="770" height="440" viewBox="0 0 770 440" aria-hidden="true">
    <line x1="38" y1="305" x2="400" y2="305" stroke="#ffffff" stroke-width="2"/>
    <line x1="400" y1="305" x2="732" y2="305" stroke="var(--rule-grey)" stroke-width="2"/>
    <polygon points="385,400 770,400 770,440 355,440" fill="var(--grey-band)"/>
  </svg>

  <div class="front-mark"><span class="square"></span>OAKLINE</div>

  <h1 class="holder-name">MARCUS HALE</h1>
  <p class="holder-role">Managing Director</p>
  <ul class="contact">
    <li class="phone">
      <svg viewBox="0 0 16 16" aria-hidden="true"><path d="M3 1.5l2.5 0 1 3.5-1.6 1.2a8 8 0 0 0 4.9 4.9l1.2-1.6 3.5 1v2.5c0 .8-.7 1.5-1.5 1.5A12 12 0 0 1 1.5 3c0-.8.7-1.5 1.5-1.5z" fill="#fff"/></svg>
      0400 318 627
    </li>
    <li class="email">
      <svg viewBox="0 0 16 16" aria-hidden="true"><rect x="1" y="3" width="14" height="10" fill="#fff"/><path d="M1 3l7 6 7-6" fill="none" stroke="#0b3f86" stroke-width="1.4"/></svg>
      mhale.office@gmail.com
    </li>
  </ul>
  <address class="address">4/18 Tide Lane<br>Port Selwyn, NSW 2999</address>
  <span class="website">www.oaklinepropertypartners.com.au</span>
</section>

<section class="card card--back" aria-label="Business card back">
  <svg class="bg" width="770" height="440" viewBox="0 0 770 440" role="img" aria-label="Large decorative brand graphic in deep blue along the left edge">
    <defs>
      <linearGradient id="backBlue" x1="0" y1="0" x2="1" y2="1">
        <stop offset="0" stop-color="#1b3a84"/>
        <stop offset="1" stop-color="#2a55a8"/>
      </linearGradient>
    </defs>
    <rect x="0" y="0" width="340" height="440" fill="url(#backBlue)"/>
  </svg>

  <div class="brand-dot" aria-hidden="true"></div>
  <p class="brand-name">OAKLINE</p>
  <p class="brand-sub">PROPERTY PARTNERS</p>
  <div class="brand-acn">A.C.N: 600 318 442</div>
  <p class="tagline"><span class="lead">Your Vision</span> <span class="rest">Our Property Partners</span></p>
</section>

</body>
</html>
```